Sandwich board

We are a Photo booth company in NZ.
We need a sandwich board design we have all the guts and we know the style we want just need help making it look good/right.
Dimension of the board are 59cm by 69cm.
The other side is a chalk board so we can write about the event we are at.
The board is a light white wash ply and we will be applying by stencil or dye cut vinyl.
The words are
Just grab a prop
and strike a pose
take your own
black and white or colour
photos
And a carriage with a camera in the back.

Reason: I would like to see a bit more of a play around with the fonts and style.

Target Market(s)

this will be at event mostly weddings, birthdays, fairs really any event.

Industry/Entity Type

Camera

Requirements
Must have
• it must be black with white back ground
Nice to have
• simple lines
Should not have
• colour. to much little detail.

```html
<!DOCTYPE html>
<html lang="en">
<head>
<meta charset="utf-8">
<title>Grab a Prop – Sandwich Board</title>
<link rel="stylesheet" href="https://fonts.googleapis.com/css2?family=Alfa+Slab+One&family=Oleo+Script:wght@700&family=Alegreya+Sans:ital,wght@1,800&family=Oswald:wght@500;700&family=Questrial&family=Old+Standard+TT&family=Playfair+Display:ital@1&display=swap">
<style>
  :root {
    --ink: #111111;
    --board: #ffffff;
    --ornament-tone: #3a3a3a;
    --illustration-tone: #555555;
  }
  html, body {
    margin: 0;
    padding: 0;
    width: 1026px;
    height: 1200px;
    overflow: hidden;
    background: var(--board);
  }
  .board {
    display: block;
    width: 1026px;
    height: 1200px;
  }
  .frame-line { stroke: var(--ink); stroke-width: 3; fill: none; }
  .rule { stroke: var(--ink); stroke-width: 3; }
  .ornament { fill: var(--ornament-tone); }
  .illustration { fill: var(--illustration-tone); }
  .ink { fill: var(--ink); }
  .slab { font-family: "Alfa Slab One", serif; font-size: 118px; fill: var(--ink); }
  .pennant-text { font-family: "Alfa Slab One", serif; font-size: 30px; fill: var(--board); }
  .and-text { font-family: "Oswald", sans-serif; font-weight: 700; font-size: 40px; fill: var(--board); }
  .script { font-family: "Oleo Script", cursive; font-weight: 700; font-size: 68px; fill: var(--ink); }
  .pose { font-family: "Alegreya Sans", sans-serif; font-style: italic; font-weight: 800; font-size: 112px; fill: var(--ink); }
  .condensed { font-family: "Oswald", sans-serif; font-weight: 500; font-size: 42px; fill: var(--ink); }
  .rounded { font-family: "Questrial", sans-serif; font-size: 44px; fill: var(--ink); letter-spacing: -1px; }
  .rounded-large { font-family: "Questrial", sans-serif; font-size: 94px; fill: var(--ink); letter-spacing: -3px; }
  .small-italic { font-family: "Playfair Display", serif; font-style: italic; font-size: 24px; fill: var(--ink); }
  .tall { font-family: "Oswald", sans-serif; font-weight: 700; font-size: 104px; fill: var(--ink); }
  .serif-display { font-family: "Old Standard TT", serif; font-size: 98px; fill: var(--ink); }
</style>
</head>
<body>
<svg class="board" viewBox="0 0 1026 1200" xmlns="http://www.w3.org/2000/svg">
  <!-- frame -->
  <line class="frame-line" x1="69" y1="42" x2="957" y2="42"/>
  <line class="frame-line" x1="69" y1="1155" x2="957" y2="1155"/>
  <line class="frame-line" x1="69" y1="260" x2="69" y2="920"/>
  <line class="frame-line" x1="957" y1="260" x2="957" y2="920"/>

  <!-- side ornaments -->
  <rect class="ornament" x="30" y="14" width="78" height="240" rx="30" role="img" aria-label="Victorian scroll ornament, top left"/>
  <rect class="ornament" x="918" y="14" width="78" height="240" rx="30" role="img" aria-label="Victorian scroll ornament, top right"/>
  <rect class="ornament" x="30" y="926" width="78" height="258" rx="30" role="img" aria-label="Victorian scroll ornament, bottom left"/>
  <rect class="ornament" x="918" y="926" width="78" height="258" rx="30" role="img" aria-label="Victorian scroll ornament, bottom right"/>

  <!-- JUST pennant -->
  <path class="ink" d="M254 79 H328 V232 L291 277 L254 232 Z"/>
  <text class="pennant-text" x="291" y="122" text-anchor="middle">J</text>
  <text class="pennant-text" x="291" y="160" text-anchor="middle">U</text>
  <text class="pennant-text" x="291" y="198" text-anchor="middle">S</text>
  <text class="pennant-text" x="291" y="236" text-anchor="middle">T</text>

  <text class="slab" x="559" y="175" text-anchor="middle" textLength="360" lengthAdjust="spacingAndGlyphs">GRAB</text>
  <text class="slab" x="555" y="277" text-anchor="middle" textLength="380" lengthAdjust="spacingAndGlyphs">A PROP</text>

  <!-- and divider -->
  <circle class="ink" cx="227" cy="349" r="5"/>
  <line class="rule" x1="250" y1="349" x2="440" y2="349"/>
  <circle class="ink" cx="499" cy="349" r="53"/>
  <circle cx="499" cy="349" r="46" fill="none" stroke="#ffffff" stroke-width="3"/>
  <text class="and-text" x="499" y="363" text-anchor="middle">and</text>
  <line class="rule" x1="558" y1="349" x2="750" y2="349"/>
  <circle class="ink" cx="774" cy="349" r="5"/>

  <text class="script" x="499" y="466" text-anchor="middle">Strike a</text>
  <line class="rule" x1="236" y1="493" x2="766" y2="493"/>
  <text class="pose" x="499" y="602" text-anchor="middle">POSE !</text>
  <line class="rule" x1="236" y1="626" x2="766" y2="626"/>

  <text class="condensed" x="502" y="684" text-anchor="middle">TAKE YOUR OWN</text>
  <text x="281" y="739"><tspan class="rounded">Black</tspan><tspan class="small-italic" dx="6">AND</tspan><tspan class="rounded" dx="4">White</tspan></text>
  <text class="rounded-large" x="279" y="830">Colour</text>
  <text class="tall" x="616" y="830">OR</text>
  <line class="rule" x1="236" y1="848" x2="766" y2="848"/>
  <text class="serif-display" x="501" y="934" text-anchor="middle">PHOTOS</text>

  <!-- carriage illustration -->
  <rect class="illustration" x="379" y="966" width="231" height="152" rx="10" role="img" aria-label="Engraved horse-drawn carriage with a large bellows camera in the back"/>
</svg>
</body>
</html>
```